RW TUBE LP
SALES SHEET
Project: RW TUBE LP
RW TUBE LP - Energy
Creative Brief
Energy
Current and potential customers. Need a professional appearance.
RW Tube- We aren’t afraid to admit we want your business, but we also aren’t afraid to do what it takes to earn it - Family owned and operated out of Midland since 1989 - Over 2 decades of leadership in the distribution of seamless and welded OCTG and Line Pipe - 30 acre storage facility located in Midland with easy interstate access - Extreme high focus on community support, leadership, and charitable activity including Halvering International and Tressler School of Midland. - Quality of service, integrity, honesty, and reputation are our core values - Small enough to be easy to deal with, yet large enough to handle any size program any where - Over 56 years of combined OCTG sales experience - We are known by the companies we keep - Great mill and vendor relationships representing several key Steel Mills - Access to premium thread connections - Inventory of internally plastic coated tubing for sour service - At the bottom contact information with titles... Dale Ormsby President Office: 555-210-4477 Cell: 555-384-1162 email: dormsby@rwtube.example Glenn Ormsby Vice President Office: 555-210-4477 Cell: 555-384-1162 email: gormsby@rwtube.example Terry Whitlock Vice President Office: 555-210-4477 Cell: 555-742-9038 email: twhitlock@rwtube.example Steven Pruitt Vice President of Sales Office: 555-210-4477 Cell: 555-617-2251 spruitt@rwtube.example Casey Lindqvist CFO Office: 555-210-4477 Cell: 555-908-3374 email: clindqvist@rwtube.example Larry Dunmore Sales and Logistics Coordinator Office: 555-210-4477 Cell: 555-455-7806 email: ldunmore@rwtube.example
LOGO AND COLOR WILL STAY THE SAME AND THE LOGO IS UP LOADED

```html
<!DOCTYPE html>
<html lang="en">
<head>
<meta charset="utf-8">
<title>RW Tube LP – Sales Sheet</title>
<link href="https://fonts.googleapis.com/css2?family=Arimo:wght@400;700&family=Open+Sans:wght@300;400;700&display=swap" rel="stylesheet">
<style>
:root{
  --red:#d41f26;
  --ink:#1a1a1a;
  --dark:#111214;
  --paper:#ffffff;
  --board:#eef0f2;
  --grey:#5b5e63;
  --sky:#6f8fb3;
  --brick:#9c6a52;
  --field:#a98a62;
  --steel:#6c7a86;
}
*{margin:0;padding:0;box-sizing:border-box}
html,body{width:1200px;height:576px;overflow:hidden;background:var(--board);font-family:"Arimo",Arial,sans-serif}
.board{position:relative;width:1200px;height:576px}
.sheet{position:absolute;top:12px;width:432px;height:528px;box-shadow:0 2px 8px rgba(0,0,0,.25)}
.sheet--front{left:132px;background:var(--dark);color:#fff}
.sheet--back{left:636px;background:var(--paper);color:var(--ink)}
.sheet-label{position:absolute;top:552px;width:432px;text-align:center;font-size:9px;letter-spacing:1px;color:var(--grey)}
.brand{display:flex;align-items:center;gap:6px;font-family:"Arimo",Arial,sans-serif;font-weight:700;color:var(--red)}
.brand-mark{width:12px;height:12px;background:var(--red)}
.sheet--front .brand{position:absolute;top:22px;left:0;right:0;justify-content:center;font-size:26px}
.photo{position:absolute}
.photo--building{left:20px;top:74px;width:392px;height:210px;background:linear-gradient(180deg,var(--sky) 0%,#aec3da 45%,var(--brick) 46%,#7d5a48 80%,#5c5c58 100%)}
.photo--yard{left:20px;top:300px;width:170px;height:210px;background:linear-gradient(180deg,#9fb5cc 0%,#c7d3de 40%,var(--field) 41%,#8a6c48 100%)}
.front-copy{position:absolute;left:202px;top:302px;width:212px}
.front-copy h2{color:var(--red);font-size:8.6px;font-weight:700;line-height:1.3;margin-bottom:8px}
.front-copy ul{list-style:none}
.front-copy li{font-size:6.4px;line-height:1.35;padding-left:8px;position:relative;margin-bottom:2px}
.front-copy li::before{content:"–";position:absolute;left:0}
.photo--pipes{left:14px;top:22px;width:150px;height:236px;background:linear-gradient(135deg,#2f3a44 0%,var(--steel) 40%,#b9c2ca 60%,#44505a 100%)}
.invite{position:absolute;left:178px;top:18px;width:240px}
.invite h1{font-family:"Open Sans",Arial,sans-serif;font-weight:300;color:var(--red);font-size:40px;line-height:1}
.invite h3{font-family:"Open Sans",Arial,sans-serif;font-size:7.6px;font-weight:700;margin:10px 0 8px}
.topics{list-style:none}
.topics li{font-size:6.6px;line-height:1.3;padding-left:9px;position:relative;margin-bottom:3px}
.topics li::before{content:"";position:absolute;left:0;top:2px;width:5px;height:5px;background:var(--red)}
.contacts{position:absolute;left:14px;top:294px;width:404px;display:grid;grid-template-columns:repeat(3,1fr);row-gap:16px;column-gap:10px}
.contact{font-size:6.2px;line-height:1.4;color:var(--grey)}
.contact .name{font-size:8px;font-weight:700;color:var(--ink)}
.contact .title{color:var(--ink);margin-bottom:2px}
.address-box{position:absolute;left:14px;top:454px;width:150px;height:40px;background:var(--red);color:#fff;font-size:6.4px;line-height:1.4;padding:8px 10px}
.sheet--back .brand{position:absolute;left:176px;top:466px;font-size:15px}
.venue{position:absolute;left:290px;top:456px;width:128px;font-size:5.8px;line-height:1.45;color:var(--grey)}
</style>
</head>
<body>
<div class="board">
  <section class="sheet sheet--front">
    <div class="brand"><span class="brand-mark"></span>RW TUBE</div>
    <div class="photo photo--building" role="img" aria-label="Photo of the RW Tube office building in Midland"></div>
    <div class="photo photo--yard" role="img" aria-label="Photo of the pipe storage yard"></div>
    <div class="front-copy">
      <h2>RW Tube – We aren’t afraid to admit we want your business, but we also aren’t afraid to do what it takes to earn it.</h2>
      <ul>
        <li>Family owned and operated out of Midland since 1989</li>
        <li>Over 2 decades of leadership in the distribution of seamless and welded OCTG and Line Pipe</li>
        <li>30 acre storage facility located in Midland with easy interstate access</li>
        <li>Extreme high focus on community support, leadership, and charitable activity including Halvering International and Tressler School of Midland</li>
        <li>Quality of service, integrity, honesty, and reputation are our core values</li>
        <li>Small enough to be easy to deal with, yet large enough to handle any size program any where</li>
        <li>Over 56 years of combined OCTG sales experience</li>
        <li>We are known by the companies we keep</li>
        <li>Great mill and vendor relationships representing several key Steel Mills</li>
        <li>Access to premium thread connections</li>
        <li>Inventory of internally plastic coated tubing for sour service</li>
      </ul>
    </div>
  </section>
  <div class="sheet-label" style="left:132px">FRONT SHEET</div>

  <section class="sheet sheet--back">
    <div class="photo photo--pipes" role="img" aria-label="Photo of stacked steel pipe ends"></div>
    <div class="invite">
      <h1>Invitation</h1>
      <h3>"SOME OF THE TOPICS TO BE DISCUSSED..."</h3>
      <ul class="topics">
        <li>ERW vs SMLS Tubs</li>
        <li>API Requirements for ERW, SEA, WELD LINE</li>
        <li>Q&amp;T material vs proprietary grades</li>
        <li>Heat treating process</li>
        <li>ERW weld line after heat treating</li>
        <li>Quality of domestic vs import mills</li>
        <li>New mills in Philippines, Mexico and Turkey and their quality</li>
        <li>What was the reasoning for so many failures in Chinese pipe</li>
        <li>Horizontal drilling and connections</li>
        <li>Mr. Hallor will also answer any questions you might have in a valuable Q&amp;A session</li>
      </ul>
    </div>
    <div class="contacts">
      <div class="contact"><div class="name">Dale Ormsby</div><div class="title">President</div>Office: 555-210-4477<br>Cell: 555-384-1162<br>email: dormsby@rwtube.example</div>
      <div class="contact"><div class="name">Terry Whitlock</div><div class="title">Vice President</div>Office: 555-210-4477<br>Cell: 555-742-9038<br>email: twhitlock@rwtube.example</div>
      <div class="contact"><div class="name">Casey Lindqvist</div><div class="title">CFO</div>Office: 555-210-4477<br>Cell: 555-908-3374<br>email: clindqvist@rwtube.example</div>
      <div class="contact"><div class="name">Glenn Ormsby</div><div class="title">Vice President</div>Office: 555-210-4477<br>Cell: 555-384-1162<br>email: gormsby@rwtube.example</div>
      <div class="contact"><div class="name">Steven Pruitt</div><div class="title">Vice President of Sales</div>Office: 555-210-4477<br>Cell: 555-617-2251<br>spruitt@rwtube.example</div>
      <div class="contact"><div class="name">Larry Dunmore</div><div class="title">Sales and Logistics Coordinator</div>Office: 555-210-4477<br>Cell: 555-455-7806<br>email: ldunmore@rwtube.example</div>
    </div>
    <div class="address-box">412 Foundry Road<br>Midland, TX 79701</div>
    <div class="brand"><span class="brand-mark"></span>RW TUBE</div>
    <p class="venue">Venue: Midland Petroleum Hall, 300 West Wall Street. Thursday, March 14. Lunch provided, 11:30 am to 2:00 pm. Seating limited, please RSVP.</p>
  </section>
  <div class="sheet-label" style="left:636px">BACK SHEET</div>
</div>
</body>
</html>
```